Restaurant menu design

Design fine dinning menu for Indian restaurant. Restaurant location is on river side. So if design has some touch of Yarra river of Melbourne and Indian touch. It is not compulsory. Creative and modern design is required.
I want to print in A3 and folded take away sizes so design should for both.
1. In A3, backside we need to design drink menu. I am attaching our current restaurant menu for drinks name and price.

Target Market(s)

Indian / Australian Customer

Industry/Entity Type

Indian Food, Indian fine dining

Colors
F0912C
F2A743
F7CA91
FBE8D2
FDF5EE

Requirements
Must have
• Simple but district design
Should not have
• common other restaurant type menu. Too many colours.

```html
<!DOCTYPE html>
<html lang="en">
<head>
<meta charset="UTF-8">
<title>Nadika Fine Dining – Menu</title>
<link href="https://fonts.googleapis.com/css2?family=Cinzel:wght@500&family=Cormorant+Garamond:ital,wght@1,500&family=Lato:wght@400;700&display=swap" rel="stylesheet">
<style>
  :root{
    --backdrop:#e8e5e0;
    --paper:#faf7f0;
    --navy:#1f3a5f;
    --gold:#c49a45;
    --muted:#6f7378;
    --mist:#cfe0e3;
    --sand:#e8d3a2;
  }
  *{margin:0;padding:0;box-sizing:border-box}
  html,body{width:1200px;height:1200px;overflow:hidden;background:var(--backdrop)}
  body{position:relative;font-family:'Lato',sans-serif;color:var(--navy)}
  .menu-card{position:absolute;left:251px;top:80px;width:722px;height:1036px;background:var(--paper);box-shadow:0 6px 18px rgba(0,0,0,.12)}
  .menu-frame{position:absolute;inset:25px;border:2px solid var(--navy)}
  .brand-dot{position:absolute;left:341px;top:96px;width:40px;height:40px;border-radius:50%;background:var(--gold)}
  .brand-name{position:absolute;left:0;right:0;top:198px;text-align:center;font-family:'Cinzel',serif;font-weight:500;font-size:38px;letter-spacing:2px;color:var(--gold)}
  .brand-tag{position:absolute;left:0;right:0;top:250px;text-align:center;font-size:15px;letter-spacing:2px;color:var(--navy)}
  .brand-sub{position:absolute;left:0;right:0;top:278px;text-align:center;font-family:'Cormorant Garamond',serif;font-style:italic;font-size:21px;color:var(--muted)}
  .river-scene{position:absolute;left:56px;top:318px;width:590px;height:158px;border-radius:40% 40% 45% 45%/30% 30% 60% 60%;
    background:linear-gradient(90deg,var(--mist) 0%,#e4eef0 45%,var(--sand) 100%);opacity:.85}
  .section-title{position:absolute;font-size:17px;font-weight:700;letter-spacing:.5px;color:var(--navy)}
  .item{position:absolute;width:255px}
  .item-name{font-size:17px;font-weight:400;color:var(--navy)}
  .item-desc{font-size:12.5px;font-style:italic;color:var(--muted);line-height:1.3;margin-top:3px}
  .item-price{position:absolute;right:0;top:1px;font-size:16px;color:var(--gold)}
  .col-left{left:75px}
  .col-right{left:372px;width:233px}
  .item-side{font-size:13px;color:var(--muted);position:absolute;right:0;top:24px}
  .footnote{position:absolute;left:0;right:0;top:968px;text-align:center;font-size:12.5px;font-style:italic;color:var(--muted)}
</style>
</head>
<body>
<main class="menu-card">
  <div class="menu-frame"></div>
  <span class="brand-dot"></span>
  <h1 class="brand-name">NADIKA</h1>
  <p class="brand-tag">FINE DINING</p>
  <p class="brand-sub">Riverside Indian Cuisine</p>
  <div class="river-scene" role="img" aria-label="Watercolour illustration of a riverside city skyline meeting domed Indian architecture along a winding river"></div>

  <h2 class="section-title col-left" style="top:522px">APPETISERS</h2>
  <div class="item col-left" style="top:562px"><p class="item-name">Samosa Chaat</p><p class="item-desc">(Spiced potato pastry, yogurt,<br>tamarind chutney)</p><span class="item-price">14</span></div>
  <div class="item col-left" style="top:630px"><p class="item-name">Paneer Tikka Skewers</p><p class="item-desc">(Marinated cheese,<br>grilled vegetables</p><span class="item-price">18</span></div>
  <div class="item col-left" style="top:699px"><p class="item-name">Lamb Shank Rogan Josh</p><p class="item-desc">(Slow-cooked, spiced,<br>dum-cooked aromatic gravy)</p><span class="item-price">38</span></div>
  <div class="item col-left" style="top:771px"><p class="item-name">Prawn Malabar</p><p class="item-desc">(Spiced prawns, coastal<br>coconut curry, spices)</p><span class="item-price">36</span></div>
  <div class="item col-left" style="top:841px"><p class="item-name">Palak Paneer</p><p class="item-desc">(Spinach purée, cottage cheese, Raita)</p><span class="item-price">26</span></div>
  <div class="item col-left" style="top:909px"><p class="item-name">Biryani</p><p class="item-desc">Naan (Plain/Garlic)</p><span class="item-price">6</span><span class="item-side" style="color:var(--gold)">5</span></div>

  <h2 class="section-title col-right" style="top:522px">TANDOORI &amp; GRILLS</h2>
  <div class="item col-right" style="top:562px"><p class="item-name">Tandoori Chicken</p><p class="item-desc">Yogurt-marinated, charred</p><span class="item-price">30</span></div>
  <div class="item col-right" style="top:630px"><p class="item-name">Seekh Kebab</p><p class="item-desc">Spiced lamb mince, skewers</p><span class="item-price">30</span></div>
  <div class="item col-right" style="top:696px"><p class="item-name">Fish Tikka</p><p class="item-desc">Ajwain-spiced, spiced,<br>grilled fish</p><span class="item-price">24</span></div>
  <h2 class="section-title col-right" style="top:758px">DESSERTS</h2>
  <div class="item col-right" style="top:794px"><p class="item-name">Mango Kulfi</p><p class="item-desc">Rich milk traditional ice cream</p><span class="item-price">12</span></div>
  <div class="item col-right" style="top:850px"><p class="item-name">Chai Crème Brûlée</p><p class="item-desc">Spiced tea</p><span class="item-price">15</span></div>
  <div class="item col-right" style="top:909px"><p class="item-name" style="font-size:14px;font-weight:700">SIDES</p><p class="item-desc">Rice (Basmati/Pulao)</p><span class="item-price">8</span><span class="item-side">Raita 8</span></div>

  <p class="footnote">Please inform us of any allergies. All prices are in AUD.</p>
</main>
</body>
</html>
```